DANLOW 'S TRUE SIMPLE NUT SPREAD Co. In need of some labels!

We need a label for a new product line. We are going to eventually need several different labels made for different types of products. As for now we are looking only for 3 product labels.

They will be:
1. Danlow's True Simple Nut Spread Smooth
2. Danlow's True Simple Nut Spread Chunky
3. Danlow's True Simple Nut Spread Honeyed

As far as colors something bright and catchy. Otherwise leaving it in the hands of the designers.

Target Market(s)

Health and fitness

Industry/Entity Type

Product

Font styles to use
Decorative
Script

Requirements
Must have
• Would like Danlow's True simple Nut spread. To stand out. So it will be easily seen on the store shelves.

```html
<!DOCTYPE html>
<html lang="en">
<head>
<meta charset="utf-8">
<title>Danlow's True Simple Nut Spread – Smooth Label</title>
<link rel="stylesheet" href="https://fonts.googleapis.com/css2?family=Archivo+Black&family=Alex+Brush&family=Arimo:wght@400;700&display=swap">
<style>
  :root {
    --backdrop: #dfe3ec;
    --band-red: #e8161b;
    --ribbon-red: #d62024;
    --ribbon-shade: #9c1417;
    --sun-light: #ffe23a;
    --sun-deep: #f6a31a;
    --oval-light: #8fd6f5;
    --oval-deep: #3aa6dc;
    --oval-edge: #2268a6;
    --navy: #1c2748;
    --white: #ffffff;
    --nut-light: #c98d4f;
    --nut-deep: #6e3f1c;
  }
  html, body {
    margin: 0;
    width: 1200px;
    height: 818px;
    overflow: hidden;
    background: var(--backdrop);
  }
  .canvas {
    position: relative;
    width: 1200px;
    height: 818px;
  }
  .label {
    position: absolute;
    left: 330px;
    top: 59px;
    width: 540px;
    height: 700px;
    display: block;
  }
  .brand-mark-text { font-family: "Arimo", sans-serif; font-weight: 700; font-size: 20px; fill: var(--navy); }
  .brand-name { font-family: "Archivo Black", sans-serif; font-size: 50px; fill: var(--band-red); letter-spacing: 1px; }
  .product-script { font-family: "Alex Brush", cursive; font-size: 74px; fill: var(--navy); stroke: var(--white); stroke-width: 5px; paint-order: stroke; }
  .product-name { font-family: "Arimo", sans-serif; font-size: 56px; fill: var(--band-red); stroke: var(--white); stroke-width: 4px; paint-order: stroke; }
  .variant { font-family: "Arimo", sans-serif; font-weight: 700; font-size: 50px; fill: var(--white); letter-spacing: 2px; }
</style>
</head>
<body>
<main class="canvas">
  <svg class="label" viewBox="0 0 540 700" xmlns="http://www.w3.org/2000/svg">
    <defs>
      <radialGradient id="sun-glow" cx="50%" cy="25%" r="75%">
        <stop offset="0" stop-color="var(--sun-light)"/>
        <stop offset="1" stop-color="var(--sun-deep)"/>
      </radialGradient>
      <linearGradient id="oval-fill" x1="0" y1="0" x2="0" y2="1">
        <stop offset="0" stop-color="var(--oval-light)"/>
        <stop offset="1" stop-color="var(--oval-deep)"/>
      </linearGradient>
      <radialGradient id="nut-fill" cx="50%" cy="55%" r="65%">
        <stop offset="0" stop-color="var(--nut-light)"/>
        <stop offset="1" stop-color="var(--nut-deep)"/>
      </radialGradient>
    </defs>

    <rect class="sun-field" x="0" y="44" width="540" height="430" fill="url(#sun-glow)" role="img" aria-label="Yellow sunburst rays radiating behind the brand oval"/>
    <rect class="nut-scene" x="0" y="460" width="540" height="196" fill="url(#nut-fill)" role="img" aria-label="Photograph of a pile of whole nuts in their shells"/>

    <rect class="band band-top" x="0" y="0" width="540" height="44" fill="var(--band-red)"/>
    <rect class="band band-bottom" x="0" y="656" width="540" height="44" fill="var(--band-red)"/>

    <g class="brand-mark">
      <rect x="212" y="60" width="34" height="34" fill="var(--white)"/>
      <text class="brand-mark-text" x="254" y="85">Danlow's</text>
    </g>

    <ellipse class="brand-oval" cx="270" cy="296" rx="246" ry="168" fill="url(#oval-fill)" stroke="var(--oval-edge)" stroke-width="3"/>

    <path class="name-banner" d="M112 186 Q270 162 428 186 L420 240 Q270 220 120 240 Z" fill="var(--white)" stroke="var(--band-red)" stroke-width="2"/>
    <text class="brand-name" x="270" y="229" text-anchor="middle">DANLOW'S</text>

    <text class="product-script" x="270" y="318" text-anchor="middle">True Simple</text>
    <text class="product-name" x="270" y="386" text-anchor="middle">Nut Spread</text>

    <g class="variant-ribbon">
      <path d="M0 426 L40 426 L40 486 L0 486 L16 456 Z" fill="var(--ribbon-shade)"/>
      <path d="M540 426 L500 426 L500 486 L540 486 L524 456 Z" fill="var(--ribbon-shade)"/>
      <path d="M22 412 Q270 398 518 412 L518 474 Q270 460 22 474 Z" fill="var(--ribbon-red)"/>
      <text class="variant" x="270" y="460" text-anchor="middle">SMOOTH</text>
    </g>
  </svg>
</main>
</body>
</html>
```